Lantern Hearthworks Business Cards

Looking to create simple business cards that highlight our unique three sided triangle fire pit design with the colors and font of our logo, listed below.

Requirements
Must have
• Looking for something simple that includes a picture of our fire pit with name, website (lanternhearthworks.com), phone number and email. Want to keep the color mostly orange and black.
• Font is gotham(medium) and orange color code is #ee6e22

```html
<!DOCTYPE html>
<html lang="en">
<head>
<meta charset="utf-8">
<title>Lantern Hearthworks Business Cards</title>
<link href="https://fonts.googleapis.com/css2?family=Montserrat:wght@400;500;600&display=swap" rel="stylesheet">
<style>
  :root {
    --orange: #ee6e22;
    --ink: #1a1a1a;
    --grey: #6d6e71;
    --grey-light: #9a9b9e;
    --paper: #ffffff;
    --backdrop: #e4e5e7;
  }
  * { box-sizing: border-box; margin: 0; padding: 0; }
  html, body { width: 1200px; height: 913px; overflow: hidden; }
  body {
    background: var(--backdrop);
    font-family: "Montserrat", sans-serif;
    position: relative;
  }
  .card {
    position: absolute;
    width: 660px;
    height: 377px;
    overflow: hidden;
    box-shadow: 0 6px 18px rgba(0,0,0,0.18);
  }
  .card--front { left: 150px; top: 60px; background: var(--paper); }
  .card--back  { left: 390px; top: 476px; background: var(--ink); }

  .card__band { position: absolute; left: 0; bottom: 0; width: 660px; height: 34px; }

  /* front */
  .brand-mark {
    position: absolute; left: 48px; top: 150px;
    display: flex; align-items: center; gap: 12px;
  }
  .brand-mark__dot {
    width: 22px; height: 22px; border-radius: 50%; background: var(--orange);
  }
  .brand-mark__name {
    font-weight: 500; font-size: 20px; color: var(--orange); letter-spacing: 0.5px;
  }
  .card__divider {
    position: absolute; left: 318px; top: 62px; width: 2px; height: 212px;
    background: var(--grey-light);
  }
  .contact {
    position: absolute; left: 346px; top: 66px; color: var(--grey);
  }
  .contact__name {
    font-weight: 600; font-size: 24px; color: var(--orange); letter-spacing: 1px;
    text-transform: uppercase; line-height: 1.1;
  }
  .contact__title { font-size: 15px; margin-bottom: 14px; }
  .contact__address { font-size: 14px; line-height: 1.35; margin-bottom: 12px; }
  .contact__list { list-style: none; font-size: 14px; line-height: 1.55; }
  .contact__list li { display: flex; align-items: center; gap: 10px; }
  .contact__icon { width: 14px; height: 14px; flex: none; }

  /* back */
  .lockup {
    position: absolute; left: 0; top: 0; width: 100%; height: 343px;
    display: flex; align-items: center; justify-content: center; gap: 26px;
  }
  .lockup__dot { width: 30px; height: 30px; border-radius: 50%; background: var(--orange); }
  .lockup__divider { width: 2px; height: 130px; background: #d9d9d9; }
  .lockup__name {
    font-weight: 500; font-size: 38px; line-height: 1.15; letter-spacing: 8px;
    color: var(--paper); text-transform: uppercase;
  }
</style>
</head>
<body>

<section class="card card--front" aria-label="Business card front">
  <div class="brand-mark">
    <span class="brand-mark__dot"></span>
    <span class="brand-mark__name">Lantern Hearthworks</span>
  </div>
  <div class="card__divider"></div>
  <div class="contact">
    <p class="contact__name">Daniel Carver</p>
    <p class="contact__title">Director</p>
    <p class="contact__address">48 Ember Lane<br>210 Halden, Norway</p>
    <ul class="contact__list">
      <li>
        <svg class="contact__icon" viewBox="0 0 16 16"><path fill="#ee6e22" d="M3.5 1.5l2.5 2.6-1.4 1.7c.9 1.9 2.4 3.4 4.3 4.3l1.7-1.4 2.6 2.5-1.4 2.3C6.8 13.2 2.8 9.2 1.3 3z"/></svg>
        5550142378
      </li>
      <li>
        <svg class="contact__icon" viewBox="0 0 16 16"><rect x="4" y="1" width="8" height="14" rx="1.5" fill="none" stroke="#ee6e22" stroke-width="1.6"/><circle cx="8" cy="12.4" r="0.9" fill="#ee6e22"/></svg>
        5550198634
      </li>
      <li>
        <svg class="contact__icon" viewBox="0 0 16 16"><rect x="1" y="3" width="14" height="10" fill="#ee6e22"/><path d="M1 3l7 6 7-6" fill="none" stroke="#fff" stroke-width="1.3"/></svg>
        info@lanternhearthworks.com
      </li>
      <li>
        <svg class="contact__icon" viewBox="0 0 16 16"><circle cx="8" cy="8" r="7" fill="#ee6e22"/><path d="M1 8h14M8 1c-3 3-3 11 0 14M8 1c3 3 3 11 0 14" fill="none" stroke="#fff" stroke-width="1"/></svg>
        www.lanternhearthworks.com
      </li>
    </ul>
  </div>
  <svg class="card__band" viewBox="0 0 660 34" preserveAspectRatio="none">
    <polygon points="0,22 400,22 412,34 0,34" fill="#ee6e22"/>
    <polygon points="412,0 660,0 660,34 412,34 400,22 412,22" fill="#6d6e71"/>
  </svg>
</section>

<section class="card card--back" aria-label="Business card back">
  <div class="lockup">
    <span class="lockup__dot"></span>
    <span class="lockup__divider"></span>
    <p class="lockup__name">Lantern<br>Hearthworks</p>
  </div>
  <svg class="card__band" viewBox="0 0 660 34" preserveAspectRatio="none">
    <polygon points="0,22 400,22 412,34 0,34" fill="#ee6e22"/>
    <polygon points="412,0 660,0 660,34 412,34 400,22 412,22" fill="#6d6e71"/>
  </svg>
</section>

</body>
</html>
```